Exciting new branding of Recruitment Company based on it's new website

We have an exciting new website we are about to launch and would like to have letterhead, business cards, email signature options, email banner, linkedin and facebook cover images all refreshed to match the website. I have attached the existing logo. The website is at http://brightcrewhire.samplehost.com/ and we are particularly interested in the grey with orange writing at the base of the first page where it says Register Now

Target Market(s)

Recruitment

Contact Information for Business Card

Dana Holt
Account Executive
T: 1300 582 317
M: 0412 637 845
E: dana@brightcrewhire.com.au
W: brightcrewhire.com.au
A: Suite 3, 42 Tamsin Court, Belwood ACT 2611
ABN: 52 418 736 904

Font styles to use
Serif
Sans Serif

Requirements
Must have
• The grey colour from the website

```html
<!DOCTYPE html>
<html lang="en">
<head>
<meta charset="utf-8">
<title>Bright Crew Hire – Business Cards</title>
<link rel="stylesheet" href="https://fonts.googleapis.com/css2?family=Mulish:wght@400;800&display=swap">
<style>
  :root {
    --backdrop: #a8a8a8;
    --card-grey: #4a4a4a;
    --card-white: #ffffff;
    --brand-orange: #f28c12;
    --text-light: #f2f2f2;
  }
  * { box-sizing: border-box; margin: 0; padding: 0; }
  html, body {
    width: 1200px; height: 857px; overflow: hidden;
    background: var(--backdrop);
    font-family: "Mulish", Arial, sans-serif;
  }
  .canvas {
    position: relative; width: 1200px; height: 857px;
    display: flex; align-items: center; justify-content: center; gap: 40px;
  }
  .card {
    position: relative; width: 540px; height: 330px;
    border-bottom: 6px solid var(--brand-orange);
    box-shadow: 0 14px 30px rgba(0,0,0,0.28);
    overflow: hidden;
  }
  .card-front { display: flex; }
  .front-brand {
    width: 46%; background: var(--card-white);
    display: flex; align-items: center; justify-content: center;
    padding: 0 20px;
  }
  .front-details {
    width: 54%; background: var(--card-grey); color: var(--text-light);
    padding: 42px 24px 0 34px;
  }
  .brand-lockup { display: flex; align-items: center; gap: 12px; }
  .brand-dot {
    width: 40px; height: 40px; border-radius: 50%;
    background: var(--brand-orange); flex: none;
  }
  .brand-name {
    color: var(--brand-orange); font-weight: 800;
    font-size: 25px; line-height: 0.95; letter-spacing: -0.4px;
    white-space: nowrap;
  }
  .contact-name { color: var(--brand-orange); font-size: 26px; font-weight: 400; line-height: 1.1; }
  .contact-title { font-size: 13px; margin-bottom: 16px; }
  .contact-address { font-size: 13px; line-height: 1.45; margin-bottom: 16px; }
  .contact-list { list-style: none; font-size: 13px; line-height: 1.6; }
  .contact-list li { display: flex; align-items: center; gap: 10px; }
  .contact-list svg { width: 12px; height: 12px; flex: none; fill: var(--brand-orange); }
  .card-back {
    background: var(--card-grey);
    display: flex; align-items: center; justify-content: center;
  }
  .card-back .brand-dot { width: 62px; height: 62px; }
  .card-back .brand-name { font-size: 40px; }
</style>
</head>
<body>
<main class="canvas">
  <section class="card card-front">
    <div class="front-brand">
      <div class="brand-lockup">
        <span class="brand-dot"></span>
        <span class="brand-name">bright crew<br>hire</span>
      </div>
    </div>
    <div class="front-details">
      <h1 class="contact-name">Dana Holt</h1>
      <p class="contact-title">Account Executive</p>
      <p class="contact-address">Suite 3, 42 Tamsin Court<br>Belwood ACT 2611</p>
      <ul class="contact-list">
        <li><svg viewBox="0 0 12 12" aria-hidden="true"><path d="M2 0.5l2.2 2.4-1 1.3c.8 1.7 2 2.9 3.6 3.7l1.3-1 2.4 2.2-1.2 2C4.9 10.6 1.4 7.1.5 1.8z"/></svg>1300 582 317</li>
        <li><svg viewBox="0 0 12 12" aria-hidden="true"><path d="M3 0h6v12H3zM4 1.5v8h4v-8z"/></svg>0412 637 845</li>
        <li><svg viewBox="0 0 12 12" aria-hidden="true"><path d="M0 2h12v8H0zM1 3l5 3.5L11 3z" fill-rule="evenodd"/></svg>dana@brightcrewhire.com.au</li>
        <li><svg viewBox="0 0 12 12" aria-hidden="true"><circle cx="6" cy="6" r="6"/></svg>brightcrewhire.com.au</li>
      </ul>
    </div>
  </section>
  <section class="card card-back">
    <div class="brand-lockup">
      <span class="brand-dot"></span>
      <span class="brand-name">bright crew<br>hire</span>
    </div>
  </section>
</main>
</body>
</html>
```